Corporate Brochure Cover Design

We need a design for a corporate A4 Size portfolio cover (front and back) which we will be distributing. to our commercial clients.

We are a professional plumbing company that is an industry leader for service we provide to our clients and technology we use. The design needs to incorporate the colours black, red, white and silver and needs to include our logo. We dont have any slogans or mottos... If you wanted to use something it could be "Delivering exceptional service...Always!" however i dont want it to b the focal point of the cover.

Im looking for something professional and modern that has the WOW factor!

Size is A4 - both front and back covers. You can include pictures as well or sample pictures of where we can source and put our own team pictures.

if you have any questions, please do not hesitate to contact me.

Target Market(s)

Our commercial & strata clients - professional industry.

Industry/Entity Type

Commercial

Font styles to use
Sans Serif

Requirements
Must have
• Red, black, white, silver as the colour scheme.
• Include the logo.
Nice to have
• Modern design and something that makes the client go WOW before they open the brochure.
Should not have
• lots of text

```html
<!DOCTYPE html>
<html lang="en">
<head>
<meta charset="utf-8">
<title>Conduit – Portfolio Cover</title>
<link href="https://fonts.googleapis.com/css2?family=Open+Sans:wght@300;400;600;700&display=swap" rel="stylesheet">
<style>
  :root {
    --silver-light: #f4f4f4;
    --silver-mid: #d9d9d9;
    --silver-dark: #bdbdbd;
    --ink: #1a1a1a;
    --text-grey: #555555;
    --logo-grey: #5a5a5a;
    --brand-red: #d0202a;
    --panel-black: #231f20;
    --white: #ffffff;
    --photo-dark: #3a3d42;
    --photo-mid: #7b8088;
  }
  * { box-sizing: border-box; margin: 0; padding: 0; }
  html, body { width: 1200px; height: 897px; overflow: hidden; background: var(--silver-mid); }
  body { font-family: "Open Sans", sans-serif; }

  .spread { position: relative; width: 1200px; height: 897px; display: flex; }

  .page {
    position: relative;
    width: 600px;
    height: 897px;
    overflow: hidden;
    background:
      repeating-linear-gradient(180deg, rgba(255,255,255,0.35) 0 1px, rgba(0,0,0,0.04) 1px 2px, rgba(255,255,255,0.15) 2px 4px),
      radial-gradient(ellipse 70% 30% at 50% 62%, var(--silver-light) 0%, rgba(244,244,244,0) 100%),
      linear-gradient(180deg, var(--silver-dark) 0%, var(--silver-mid) 35%, var(--silver-light) 62%, var(--silver-mid) 100%);
  }
  .page--back::after {
    content: ""; position: absolute; top: 0; right: 0; width: 90px; height: 100%;
    background: linear-gradient(90deg, rgba(0,0,0,0) 0%, rgba(0,0,0,0.08) 100%);
    z-index: 3;
  }
  .page--front::before {
    content: ""; position: absolute; top: 0; left: 0; width: 40px; height: 100%;
    background: linear-gradient(90deg, rgba(0,0,0,0.1) 0%, rgba(0,0,0,0) 100%);
    z-index: 3;
  }

  .brand {
    position: absolute; display: flex; align-items: center; gap: 8px;
    font-weight: 700; letter-spacing: 0.5px;
  }
  .brand__dot { width: 14px; height: 14px; border-radius: 50%; flex: none; }

  .brand--header { left: 44px; top: 58px; font-size: 26px; color: var(--logo-grey); }
  .brand--header .brand__dot { background: var(--logo-grey); }

  .divider {
    position: absolute; left: 260px; top: 42px; width: 1px; height: 82px;
    background: var(--text-grey);
  }

  .contact {
    position: absolute; left: 296px; top: 52px;
    font-size: 12.5px; line-height: 19px; color: var(--text-grey); font-style: normal;
  }
  .contact__title { font-weight: 600; }

  /* Back cover: supporting photo strip and dark base band */
  .back-photo {
    position: absolute; left: 44px; right: 44px; top: 520px; height: 200px;
    background: linear-gradient(135deg, var(--photo-dark) 0%, var(--photo-mid) 100%);
  }
  .base-band {
    position: absolute; left: 0; right: 0; bottom: 0; height: 86px;
    background: var(--panel-black);
    border-top: 4px solid var(--brand-red);
  }

  .tagline {
    position: absolute; left: 56px; top: 42px;
    font-weight: 300; font-size: 35px; line-height: 42px; color: var(--ink);
  }
  .tagline__accent { color: var(--brand-red); }

  /* Front cover: hero photo with red and black accent bands */
  .hero-photo {
    position: absolute; left: 0; right: 0; top: 190px; height: 440px;
    background: linear-gradient(160deg, var(--photo-mid) 0%, var(--photo-dark) 100%);
  }
  .accent-line {
    position: absolute; left: 0; right: 0; top: 630px; height: 8px;
    background: var(--brand-red);
  }
  .accent-band {
    position: absolute; left: 0; right: 0; top: 638px; height: 20px;
    background: var(--panel-black);
  }

  .brand-panel {
    position: absolute; right: 0; top: 709px; width: 194px; height: 102px;
    background: var(--panel-black);
  }
  .brand--panel { left: 22px; top: 36px; font-size: 22px; color: var(--white); }
  .brand--panel .brand__dot { background: var(--brand-red); }
</style>
</head>
<body>
  <main class="spread">
    <section class="page page--back" aria-label="Back cover">
      <div class="brand brand--header"><span class="brand__dot"></span>CONDUIT</div>
      <div class="divider"></div>
      <address class="contact">
        <p class="contact__title">CONTACT US</p>
        <p>T. 088 41 305</p>
        <p>info@conduitpro.com</p>
      </address>
      <div class="back-photo" role="img" aria-label="Photograph of the plumbing team on a commercial site"></div>
      <div class="base-band"></div>
    </section>

    <section class="page page--front" aria-label="Front cover">
      <h1 class="tagline">Delivering exceptional<br>service... <span class="tagline__accent">Always!</span></h1>
      <div class="hero-photo" role="img" aria-label="Photograph of modern commercial plumbing work and technology"></div>
      <div class="accent-line"></div>
      <div class="accent-band"></div>
      <div class="brand-panel">
        <div class="brand brand--panel"><span class="brand__dot"></span>CONDUIT</div>
      </div>
    </section>
  </main>
</body>
</html>
```